Infectious Diseases Research Laboratory Needs Business Card

We need a business card for an academic research laboratory based in Kansas City called MORVEK. The full lab name is Microbial Dose-Response/Exposure Bridging Studies Laboratory, but this does not need to be incorporated. We study novel ways to optimize the treatment of multidrug-resistant bacterial infections ("superbugs") throughout the entire biomedical research spectrum (from benchtop to bedside). The name MORVEK is not only an acronym for our lab name, but also represents our desire to make discoveries and explore the unknown (the stars, if you well). It also serves as an ode to the state of Kansas motto where we are based, ad astra per aspera ("to the stars, through difficulty").

Target Market(s)

Pharmaceutical companies, researchers

Industry/Entity Type

Pharmaceutical

Contact Information for Business Card

The business card should incorporate and complement our new logo (see uploaded files). Double-sided designs are preferred. Looking for something modern, but professional.

Font styles to use
Sans Serif

Requirements
Must have
• Double-sided. One side would ideally be a solid color incorporating logo and the other should also have the logo (smaller), but incorporate staff information.
• Color codes:
• Red: #F04C51
• Blue: #3477B5
• Gray: #808285

```html
<!DOCTYPE html>
<html lang="en">
<head>
<meta charset="utf-8">
<title>MORVEK Business Card</title>
<link rel="stylesheet" href="https://fonts.googleapis.com/css2?family=Lato:wght@400;700&display=swap">
<style>
  :root {
    --red: #F04C51;
    --red-deep: #C43A40;
    --blue: #3477B5;
    --gray: #808285;
    --ink: #6d6e71;
    --white: #ffffff;
    --paper: #f4f4f4;
    --stage: #e6e7e8;
  }
  * { box-sizing: border-box; margin: 0; padding: 0; }
  html, body {
    width: 1200px; height: 900px; overflow: hidden;
    background: var(--stage);
    font-family: "Lato", "Helvetica Neue", Arial, sans-serif;
  }
  .canvas { position: relative; width: 1200px; height: 900px; }

  .card {
    position: absolute; width: 700px; height: 400px;
    background: var(--white); overflow: hidden;
    box-shadow: 0 10px 28px rgba(0,0,0,0.18);
  }
  .card-front { left: 80px; top: 45px; background: linear-gradient(160deg, var(--white), var(--paper)); }
  .card-back  { left: 420px; top: 465px; }
  .card-shapes { position: absolute; inset: 0; width: 700px; height: 400px; }

  .wordmark {
    position: absolute; display: flex; align-items: center;
    font-weight: 400; line-height: 1; white-space: nowrap;
  }
  .wordmark-dot { border-radius: 50%; flex: none; }
  .front-wordmark { left: 130px; top: 92px; gap: 14px; font-size: 46px; letter-spacing: 6px; color: var(--red); }
  .front-wordmark .wordmark-dot { width: 24px; height: 24px; background: var(--blue); }
  .back-wordmark { left: 36px; top: 104px; gap: 12px; font-size: 38px; letter-spacing: 5px; color: var(--white); }
  .back-wordmark .wordmark-dot { width: 22px; height: 22px; background: var(--white); }

  .front-url {
    position: absolute; left: 0; right: 0; top: 305px; text-align: center;
    color: var(--white); font-size: 17px; letter-spacing: 0.5px;
  }

  .staff { position: absolute; left: 470px; top: 62px; width: 215px; }
  .staff-name { font-size: 25px; font-weight: 700; letter-spacing: 0.3px; line-height: 1; white-space: nowrap; }
  .staff-name .given { color: var(--red); }
  .staff-name .family { color: var(--blue); font-weight: 400; }
  .staff-role { margin-top: 6px; color: var(--blue); font-size: 15px; letter-spacing: 0.5px; }
  .staff-rule { margin-top: 10px; width: 160px; height: 4px; background: var(--red); }

  .contact-list { list-style: none; margin-top: 22px; }
  .contact-item { display: flex; align-items: center; gap: 12px; margin-bottom: 16px; }
  .contact-icon { width: 28px; height: 28px; flex: none; }
  .contact-text { color: var(--ink); font-size: 14px; line-height: 1.3; white-space: nowrap; }
</style>
</head>
<body>
<main class="canvas">

  <section class="card card-front" aria-label="Card front">
    <svg class="card-shapes" viewBox="0 0 700 400" aria-hidden="true">
      <defs>
        <linearGradient id="frontRed" x1="0" y1="1" x2="1" y2="0">
          <stop offset="0" stop-color="#C43A40"/>
          <stop offset="1" stop-color="#F04C51"/>
        </linearGradient>
      </defs>
      <path d="M0 290 C 250 250 500 150 700 40 V 54 C 500 164 250 264 0 304 Z" fill="#3477B5"/>
      <path d="M0 304 C 250 264 500 164 700 54 V 400 H 0 Z" fill="url(#frontRed)"/>
    </svg>
    <div class="wordmark front-wordmark"><span class="wordmark-dot"></span>MORVEK</div>
    <p class="front-url">www.morveklab.org</p>
  </section>

  <section class="card card-back" aria-label="Card back">
    <svg class="card-shapes" viewBox="0 0 700 400" aria-hidden="true">
      <defs>
        <linearGradient id="backRed" x1="0" y1="0" x2="0" y2="1">
          <stop offset="0" stop-color="#F04C51"/>
          <stop offset="1" stop-color="#C43A40"/>
        </linearGradient>
      </defs>
      <path d="M0 0 H 324 C 380 110 420 260 454 400 H 0 Z" fill="#3477B5"/>
      <path d="M0 0 H 310 C 366 110 406 260 440 400 H 0 Z" fill="url(#backRed)"/>
    </svg>
    <div class="wordmark back-wordmark"><span class="wordmark-dot"></span>MORVEK</div>
    <svg class="card-shapes" viewBox="0 0 700 400" role="img" aria-label="Faint line illustration of two laboratory flasks">
      <rect x="70" y="195" width="250" height="185" rx="24" fill="#ffffff" fill-opacity="0.08"/>
    </svg>

    <div class="staff">
      <h1 class="staff-name"><span class="given">HALVARD</span> <span class="family">REESE</span></h1>
      <p class="staff-role">WEB DESIGNER</p>
      <div class="staff-rule"></div>
      <ul class="contact-list">
        <li class="contact-item">
          <svg class="contact-icon" viewBox="0 0 30 30" aria-hidden="true">
            <circle cx="15" cy="15" r="15" fill="#3477B5"/>
            <path d="M10 9 L13 9 L14 12 L12.5 13.5 C13.5 15.5 14.5 16.5 16.5 17.5 L18 16 L21 17 L21 20 C21 20.6 20.6 21 20 21 C14 21 9 16 9 10 C9 9.4 9.4 9 10 9 Z" fill="#ffffff"/>
          </svg>
          <p class="contact-text">+1 816 555 0142<br>+1 816 555 0187</p>
        </li>
        <li class="contact-item">
          <svg class="contact-icon" viewBox="0 0 30 30" aria-hidden="true">
            <circle cx="15" cy="15" r="15" fill="#3477B5"/>
            <rect x="8" y="10" width="14" height="10" rx="1" fill="#ffffff"/>
            <path d="M8.5 10.5 L15 15.5 L21.5 10.5" fill="none" stroke="#3477B5" stroke-width="1.3"/>
          </svg>
          <p class="contact-text">info@morveklab.org<br>www.morveklab.org</p>
        </li>
        <li class="contact-item">
          <svg class="contact-icon" viewBox="0 0 30 30" aria-hidden="true">
            <circle cx="15" cy="15" r="15" fill="#3477B5"/>
            <path d="M15 7 C11.7 7 9.5 9.4 9.5 12.4 C9.5 16.2 15 23 15 23 C15 23 20.5 16.2 20.5 12.4 C20.5 9.4 18.3 7 15 7 Z" fill="#ffffff"/>
            <circle cx="15" cy="12.5" r="2.2" fill="#3477B5"/>
          </svg>
          <p class="contact-text">4120 Lindell Way,<br>Kansas City, MO 64110</p>
        </li>
      </ul>
    </div>
  </section>

</main>
</body>
</html>
```